Radiant Venture Informational Sheet

I need a one page informational sheet (advertisement) for a horse called Radiant Venture. It should have the name Radiant Venture and the content below. It needs to be eye-catching. I have attached 3 examples of what these advertisements look like so it's easier to create. I've also attached 2 pictures of the horse which should both be used in the advertisement.

Here are the bullet points:

- Son of Gallant Harbor with total progeny earnings over 13 million dollars
- Ranks among West Virginia top 3 active sires by progeny earnings 2019
- In 9 crops of racing age, has sired 200 winners from 275 starters
- Sired Sr. Montevarro who earned over $800k racing from age 2 to 7.
- Won 3 of 4 lifetime starts

stands at stud for $1000 at Ashgrove Farm near Charles Town
Call Dale Harwick - (304) 555-0193

Target Market(s)

Thoroughbred racing people interested in breeding

Requirements
Must have
• Unique and creative. The name of the horse Radiant Venture should be clear and bold, the picture should also be prominent.
Should not have
• Cartoon like, whimsical

```html
<!DOCTYPE html>
<html lang="en">
<head>
<meta charset="utf-8">
<title>Radiant Venture – Stallion Sheet</title>
<link rel="stylesheet" href="https://fonts.googleapis.com/css2?family=Michroma&family=Oswald:wght@300;400;500;600&family=Playfair+Display:ital,wght@1,700&family=Roboto+Slab:wght@700&display=swap">
<style>
  :root {
    --ground: #2d1915;
    --ground-deep: #24130f;
    --gold: #f29b2c;
    --gold-soft: #f6b055;
    --rust: #a8592d;
    --cream: #fbeee0;
    --white: #ffffff;
  }
  html, body { margin: 0; padding: 0; overflow: hidden; }
  body { width: 939px; height: 1200px; background: var(--ground); }
  .sheet {
    position: relative; width: 939px; height: 1200px; overflow: hidden;
    background: linear-gradient(180deg, var(--ground-deep), var(--ground) 40%);
    font-family: "Oswald", sans-serif;
  }
  .masthead {
    position: absolute; left: 62px; top: 40px;
    font-family: "Michroma", sans-serif; font-size: 33px; letter-spacing: 1px; line-height: 1.2;
    color: var(--gold); margin: 0; font-weight: 400; white-space: nowrap;
  }
  .masthead-rule { position: absolute; left: 552px; right: 0; top: 64px; height: 4px; background: var(--white); }
  .hero-art { position: absolute; left: 0; top: 0; width: 939px; height: 1200px; }

  .hero-claim { position: absolute; left: 22px; top: 455px; width: 300px; height: 175px; }
  .hero-claim span { position: absolute; white-space: nowrap; line-height: 1; }
  .claim-side {
    left: 14px; top: 150px; transform: rotate(-90deg); transform-origin: left top;
    color: var(--white); font-size: 17px; font-weight: 500; letter-spacing: 1px;
  }
  .claim-top { left: 30px; top: 0; color: var(--gold); font-size: 31px; font-weight: 400; letter-spacing: 0.5px; }
  .claim-over {
    left: 30px; top: 32px; width: 240px; text-align: center;
    font-family: "Playfair Display", serif; font-style: italic; font-weight: 700;
    color: var(--gold); font-size: 28px;
  }
  .hero-claim .claim-over::before, .hero-claim .claim-over::after { content: ""; position: absolute; top: 15px; width: 45px; height: 2px; background: var(--white); }
  .claim-over::before { left: 6px; } .claim-over::after { right: 6px; }
  .claim-big {
    left: 30px; top: 60px; color: var(--white); font-size: 72px; font-weight: 400;
    transform: scaleX(0.7); transform-origin: left top; letter-spacing: 1px;
  }
  .claim-unit { left: 34px; top: 140px; color: var(--gold); font-size: 26px; font-weight: 600; letter-spacing: 16px; }

  .portrait {
    position: absolute; left: 12px; top: 697px; width: 312px; height: 406px;
    border: 3px solid var(--white); border-radius: 36px; overflow: hidden;
    background: linear-gradient(160deg, #5a6468 0%, #3c4245 35%, #7a3c1c 60%, #a4552a 100%);
  }
  .portrait-claim { position: absolute; left: 24px; bottom: 14px; width: 190px; height: 140px; }
  .portrait-claim span { position: absolute; white-space: nowrap; line-height: 1; }
  .won { left: 30px; top: 2px; font-family: "Playfair Display", serif; font-style: italic; font-weight: 700; color: var(--white); font-size: 30px; }
  .tally { left: 0; top: 38px; color: var(--gold); font-size: 72px; transform: scaleX(0.7); transform-origin: left top; }
  .starts { left: 186px; top: 34px; color: var(--gold); font-size: 34px; transform: rotate(90deg); transform-origin: left top; letter-spacing: 1px; }
  .lifetime { left: 4px; top: 114px; color: var(--white); font-size: 20px; font-weight: 500; letter-spacing: 2px; }

  .facts-title {
    position: absolute; left: 546px; top: 705px; width: 364px; height: 46px; box-sizing: border-box;
    border: 3px solid var(--gold); border-radius: 12px; background: var(--rust);
    font-family: "Michroma", sans-serif; font-size: 21px; color: var(--cream);
    display: flex; align-items: center; justify-content: center; margin: 0; font-weight: 400;
  }
  .facts-spine { position: absolute; left: 727px; top: 751px; width: 4px; height: 260px; background: var(--white); }
  .fact-list { list-style: none; margin: 0; padding: 0; }
  .fact {
    position: absolute; height: 34px; box-sizing: border-box; border-radius: 10px;
    display: flex; align-items: center; justify-content: center;
    font-size: 16px; font-weight: 300; white-space: nowrap;
    box-shadow: 0 3px 6px rgba(0,0,0,0.5);
  }
  .fact--gold { background: var(--gold); color: var(--ground); font-weight: 400; }
  .fact--rust { background: var(--rust); color: var(--cream); }
  .stud-rule { position: absolute; left: 366px; top: 1054px; width: 530px; height: 2px; background: var(--white); }
  .stud-note { position: absolute; left: 366px; top: 1064px; width: 530px; text-align: center; font-family: "Roboto Slab", serif; font-weight: 700; color: var(--white); font-size: 13px; margin: 0; white-space: nowrap; }
  .stud-call { position: absolute; left: 366px; top: 1084px; width: 530px; text-align: center; font-family: "Roboto Slab", serif; font-weight: 700; color: var(--white); font-size: 19px; margin: 0; letter-spacing: 0.5px; white-space: nowrap; }
  .footer-band { position: absolute; left: 0; bottom: 0; width: 939px; height: 40px; }
</style>
</head>
<body>
<main class="sheet">
  <h1 class="masthead">RADIANT VENTURE</h1>
  <div class="masthead-rule"></div>

  <svg class="hero-art" viewBox="0 0 939 1200">
    <defs>
      <linearGradient id="heroTone" x1="0" y1="0" x2="0" y2="1">
        <stop offset="0" stop-color="#c9c4bd"/>
        <stop offset="0.35" stop-color="#9a6a4c"/>
        <stop offset="0.6" stop-color="#7a3a1a"/>
        <stop offset="0.75" stop-color="#3e4a6a"/>
        <stop offset="1" stop-color="#2c3656"/>
      </linearGradient>
      <filter id="glow" x="-20%" y="-20%" width="140%" height="140%">
        <feGaussianBlur stdDeviation="5"/>
      </filter>
    </defs>
    <path role="img" aria-label="Photograph of Radiant Venture, a bay stallion, standing in profile on a paved yard before a brick barn and bare trees"
      d="M0 170 C10 122 40 110 100 108 L740 108 A170 170 0 0 1 910 278 L910 520 A165 165 0 0 1 745 685 L0 685 Z"
      fill="url(#heroTone)"/>
    <path d="M740 108 A170 170 0 0 1 910 278 L910 520 A165 165 0 0 1 745 685" fill="none" stroke="#f29b2c" stroke-width="8" filter="url(#glow)"/>
    <path d="M740 108 A170 170 0 0 1 910 278 L910 520 A165 165 0 0 1 745 685" fill="none" stroke="#f29b2c" stroke-width="3"/>
    <path d="M0 170 C10 122 40 110 100 108 L740 108" fill="none" stroke="#ffffff" stroke-width="2"/>
  </svg>

  <div class="hero-claim">
    <span class="claim-side">WITH TOTAL</span>
    <span class="claim-top">PROGENY EARNINGS</span>
    <span class="claim-over">Of Over</span>
    <span class="claim-big">13 MILLION</span>
    <span class="claim-unit">DOLLARS</span>
  </div>

  <div class="portrait" role="img" aria-label="Head and shoulders photograph of Radiant Venture wearing a halter, in front of a stable window">
    <div class="portrait-claim">
      <span class="won">Won</span>
      <span class="tally">3 OF 4</span>
      <span class="starts">STARTS</span>
      <span class="lifetime">LIFETIME</span>
    </div>
  </div>

  <h2 class="facts-title">RADIANT VENTURE</h2>
  <div class="facts-spine"></div>
  <ul class="fact-list">
    <li class="fact fact--gold" style="left:357px; top:777px; width:516px;">- Son of Gallant Harbor with total progeny earnings over 13 million dollars</li>
    <li class="fact fact--rust" style="left:392px; top:833px; width:516px;">- Ranks among West Virginia top 3 active sires by progeny earnings 2019</li>
    <li class="fact fact--gold" style="left:357px; top:886px; width:513px;">- In 9 crops of racing age, has sired 200 winners from 275 starters</li>
    <li class="fact fact--rust" style="left:401px; top:943px; width:509px;">- Sired Sr. Montevarro who earned over $800k racing from age 2 to 7</li>
    <li class="fact fact--gold" style="left:518px; top:995px; width:232px;">- Won 3 of 4 lifetime starts</li>
  </ul>

  <div class="stud-rule"></div>
  <p class="stud-note">Stands at stud for $1000 at Ashgrove Farm near Charles Town</p>
  <p class="stud-call">Call Dale Harwick - (304) 555-0193</p>

  <svg class="footer-band" viewBox="0 0 939 40" preserveAspectRatio="none" aria-hidden="true">
    <rect x="0" y="0" width="939" height="40" fill="#f29b2c"/>
    <polygon points="470,40 540,0 939,0 939,40" fill="#a8592d"/>
  </svg>
</main>
</body>
</html>
```